Book cover for ebook and Physical book for Mind Clutter Collective

I run a non-profit Mind Clutter Collective and I have a new book that needs a cover. For the physical book, I will need a full wrap. The mission is to help individuals Quiet the cycle of restless worry patterns. This book is title is "Quiet the cycle of restless worry patterns", and subtitle "Clear Your Mind of Static Noise." I am open to anything design wise, nothing is set in stone. Oh, MCC is pending Trademark.

Target Market(s)

Typically it's Mom's from 25-40

Industry/Entity Type

Mental Health

Font styles to use
Serif

Colors
f37122
9bcb3b
fbed22
0255a3
e34197

Requirements
Must have
• I do like simplicity, yet vibrant colors.
Nice to have
• The authors are Rex T. Whitford, and Dana Okonkwo. For some inspiration individuals refer to me as the Wonder Guide having reversed five incurable diseases.
Should not have
• The cover shouldn't be too busy.

```html
<!DOCTYPE html>
<html lang="en">
<head>
<meta charset="utf-8">
<title>Quiet the cycle of restless worry patterns — Book Cover</title>
<link rel="stylesheet" href="https://fonts.googleapis.com/css2?family=Lora:ital,wght@1,700&family=Tinos&display=swap">
<style>
  :root {
    --page: #ffffff;
    --blue: #0255a3;
    --blue-light: #1f6bb5;
    --green: #9bcb3b;
    --photo-top: #d4d3cc;
    --photo-mid: #b6b0a1;
    --photo-bottom: #6c6155;
    --band-orange: rgba(243, 113, 34, 0.55);
    --band-green: rgba(120, 150, 20, 0.65);
    --band-blue: rgba(2, 60, 120, 0.6);
    --band-pink: rgba(227, 65, 120, 0.5);
    --subtitle-band: rgba(255, 255, 255, 0.22);
    --text-light: #ffffff;
    --title-font: "Lora", Georgia, serif;
    --body-font: "Tinos", "Times New Roman", serif;
  }
  * { margin: 0; padding: 0; box-sizing: border-box; }
  html, body {
    width: 1200px; height: 1000px; overflow: hidden;
    background: var(--page);
    font-family: var(--body-font);
  }
  .cover {
    position: absolute; left: 258px; top: 2px;
    width: 685px; height: 995px; overflow: hidden;
    box-shadow: 0 0 2px rgba(0,0,0,0.35);
  }
  .cover-photo {
    position: absolute; inset: 0;
    background: linear-gradient(180deg, var(--photo-top) 0%, var(--photo-mid) 55%, var(--photo-bottom) 100%);
  }
  .header-shapes { position: absolute; left: 0; top: 0; }
  .authors-rule {
    position: absolute; left: 420px; top: 28px;
    width: 6px; height: 60px; background: rgba(255,255,255,0.45);
  }
  .authors {
    position: absolute; right: 18px; top: 25px;
    color: var(--text-light); font-size: 28px; line-height: 36px;
    text-align: right; font-weight: 400;
  }
  .title { position: absolute; left: 0; top: 435px; width: 685px; font-family: var(--title-font); }
  .title-line {
    position: absolute; right: 0; height: 64px;
    color: var(--text-light); font-style: italic; font-weight: 700;
    font-size: 48px; line-height: 62px; padding-left: 8px;
    white-space: nowrap;
  }
  .title-line--1 { top: 0;    left: 279px; background: var(--band-orange); }
  .title-line--2 { top: 68px;  left: 322px; background: var(--band-green); padding-left: 26px; }
  .title-line--3 { top: 138px; left: 345px; background: var(--band-blue); padding-left: 34px; height: 60px; line-height: 58px; }
  .title-line--4 { top: 204px; left: 345px; background: var(--band-pink); padding-left: 18px; height: 48px; line-height: 46px; }
  .subtitle {
    position: absolute; left: 87px; top: 903px; width: 513px; height: 42px;
    background: var(--subtitle-band);
    color: var(--text-light); font-size: 29px; line-height: 42px;
    text-align: center; white-space: nowrap;
  }
</style>
</head>
<body>
  <main class="cover">
    <div class="cover-photo" role="img" aria-label="Cover photograph: a woman seen from behind meditating on a wooden dock by a calm lake"></div>

    <svg class="header-shapes" width="685" height="270" viewBox="0 0 685 270" aria-hidden="true">
      <polygon points="0,0 0,195 217,128" fill="var(--green)"/>
      <polygon points="4,0 685,0 685,183 437,256" fill="var(--blue)"/>
      <polygon points="4,0 685,0 685,120 470,218" fill="var(--blue-light)" opacity="0.55"/>
      <polyline points="4,0 437,256 685,183" fill="none" stroke="#ffffff" stroke-width="2"/>
    </svg>

    <div class="authors-rule"></div>
    <p class="authors">Rex T. Whitford &amp;<br>Dana Okonkwo</p>

    <h1 class="title">
      <span class="title-line title-line--1">Quiet the cycle</span>
      <span class="title-line title-line--2">of restless</span>
      <span class="title-line title-line--3">worry</span>
      <span class="title-line title-line--4">patterns</span>
    </h1>

    <p class="subtitle">Clear Your Mind of Static Noise</p>
  </main>
</body>
</html>
```